Banner Ads, Icons, Logos, Photos for Chamber of Commerce

We just joined a chamber of commerce. I need several items made up with our logo and branding. We do not have a copy of our logo in large format. All logo and colors can be found on our website: http://www.myridgelinerails.example

2 Banner ads – 480 pixels w x 60 pixels h and 72 dpi in jpg or png
1 Homepage ad – 600 pixels w x 100 pixels h and 72 dpi in jpg or png
1 Search Results Icon max size is 75 x 75 pixels 72 dpi in jpg or png
1 Logo max size is 150 pixels w x 100 pixels h 72 dpi in jpg or png
1 Member Page photos max size is 600 x 600 pixels 72 dpi in jpg or png.
1 Thumbnail size is 150 x 150 pixels.

Industry/Entity Type

Residential Construction

Font styles to use
Sans Serif

Colors
0392cd
34a6d7
85cae6
cfe9f4
fbf289
fbee3d
cfdeed
85acd3

Requirements
Must have
• Logo
• phone number ( 555-316-2047 )
• "Free Estimates"
Nice to have
• Fence Photos - 1 wood fence photo, 1 aluminum fence photo, 1 vinyl fence photo
Should not have
• Too many words, too many colors

```html
<!DOCTYPE html>
<html lang="en">
<head>
<meta charset="utf-8">
<title>Ridgeline Rails – Chamber Member Kit</title>
<link rel="stylesheet" href="https://fonts.googleapis.com/css2?family=Open+Sans:ital,wght@0,400;0,600;0,700;1,700&display=swap">
<style>
  :root {
    --canvas: #edeff1;
    --orange: #f7881f;
    --orange-light: #fbb116;
    --blue: #0a7fc4;
    --brown: #5a3a22;
    --ink: #2f2f2f;
    --white: #ffffff;
    --wood-a: #b58d55;
    --wood-b: #d9b97c;
    --grass: #7c9a52;
    --mist-a: #dfe4e0;
    --mist-b: #eef1ee;
    --vinyl-a: #6f8d4a;
    --vinyl-b: #e9ecec;
    --portrait-a: #c9b8a4;
    --portrait-b: #2a2d38;
  }
  html, body { margin: 0; padding: 0; overflow: hidden; }
  body { width: 1200px; height: 1000px; background: var(--canvas); font-family: "Open Sans", sans-serif; }
  .kit { display: block; width: 1200px; height: 1000px; }
  .brand-name { font-family: "Open Sans", sans-serif; font-weight: 700; fill: var(--blue); }
  .brand-name-dark { font-family: "Open Sans", sans-serif; font-weight: 700; fill: var(--brown); }
  .contact { font-family: "Open Sans", sans-serif; font-weight: 400; fill: var(--ink); }
  .cta-text { font-family: "Open Sans", sans-serif; font-weight: 600; fill: var(--white); }
  .cta-frame { fill: none; stroke: var(--white); stroke-width: 1.2; }
  .phone-bold { font-family: "Open Sans", sans-serif; font-weight: 700; fill: #111; }
  .tagline { font-family: "Open Sans", sans-serif; font-weight: 700; font-style: italic; fill: #111; }
  .member-name { font-family: "Open Sans", sans-serif; font-weight: 700; fill: var(--brown); }
  .member-role { font-family: "Open Sans", sans-serif; font-weight: 400; fill: var(--orange); letter-spacing: 2px; }
</style>
</head>
<body>
<svg class="kit" viewBox="0 0 1200 1000" xmlns="http://www.w3.org/2000/svg">
  <defs>
    <linearGradient id="wood" x1="0" y1="0" x2="1" y2="1">
      <stop offset="0" stop-color="var(--grass)"/>
      <stop offset="0.3" stop-color="var(--wood-b)"/>
      <stop offset="1" stop-color="var(--wood-a)"/>
    </linearGradient>
    <linearGradient id="mist" x1="0" y1="0" x2="1" y2="0">
      <stop offset="0" stop-color="var(--mist-a)"/>
      <stop offset="1" stop-color="var(--mist-b)"/>
    </linearGradient>
    <linearGradient id="vinyl" x1="0" y1="0" x2="0" y2="1">
      <stop offset="0" stop-color="var(--vinyl-a)"/>
      <stop offset="0.35" stop-color="var(--vinyl-b)"/>
      <stop offset="1" stop-color="var(--vinyl-a)"/>
    </linearGradient>
    <linearGradient id="portrait" x1="0" y1="0" x2="0" y2="1">
      <stop offset="0" stop-color="var(--portrait-a)"/>
      <stop offset="1" stop-color="var(--portrait-b)"/>
    </linearGradient>
    <symbol id="phone-icon" viewBox="0 0 16 16">
      <path d="M3.5 1.5l2.5 0 1.2 3.2-1.6 1.2c.8 1.8 2.2 3.2 4 4l1.2-1.6 3.2 1.2 0 2.5c0 .8-.7 1.5-1.5 1.5C6.8 13.5 2 8.7 2 3c0-.8.7-1.5 1.5-1.5z" fill="var(--blue)"/>
    </symbol>
    <symbol id="mail-icon" viewBox="0 0 16 12">
      <rect x="0" y="0" width="16" height="12" rx="1.5" fill="var(--blue)"/>
      <path d="M1 1.5l7 5 7-5" fill="none" stroke="var(--white)" stroke-width="1.4"/>
    </symbol>
  </defs>

  <!-- Banner ad A -->
  <g class="banner banner-a">
    <rect x="70" y="52" width="720" height="90" fill="var(--white)"/>
    <rect x="70" y="52" width="300" height="90" fill="url(#wood)" role="img" aria-label="Photo of a wooden picket fence on grass"/>
    <polygon points="255,52 345,52 378,142 290,142" fill="var(--orange-light)"/>
    <polygon points="340,52 378,52 412,142 370,142" fill="var(--orange)"/>
    <rect x="408" y="133" width="382" height="9" fill="var(--orange)"/>
    <rect x="97" y="79" width="201" height="42" class="cta-frame"/>
    <text x="197" y="108" text-anchor="middle" class="cta-text" font-size="23">Free Estimates</text>
    <circle cx="472" cy="72" r="5" fill="var(--orange)"/>
    <text x="483" y="78" class="brand-name" font-size="16">Ridgeline Rails</text>
    <use href="#phone-icon" x="485" y="87" width="15" height="15"/>
    <text x="508" y="101" class="contact" font-size="16">555-316-2047</text>
    <use href="#mail-icon" x="485" y="111" width="16" height="12"/>
    <text x="508" y="124" class="contact" font-size="16">office@myridgelinerails.example</text>
  </g>

  <!-- Banner ad B -->
  <g class="banner banner-b">
    <rect x="70" y="171" width="720" height="90" fill="url(#mist)" role="img" aria-label="Faded photo of trees behind a white vinyl fence"/>
    <polygon points="495,171 790,171 790,261 465,261" fill="url(#wood)" role="img" aria-label="Photo of a wooden fence"/>
    <polygon points="470,206 505,206 465,261 432,261" fill="var(--brown)"/>
    <polygon points="505,171 520,171 480,261 465,261" fill="var(--blue)"/>
    <polygon points="518,171 670,171 640,261 482,261" fill="var(--orange)" opacity="0.9"/>
    <rect x="559" y="197" width="200" height="42" class="cta-frame"/>
    <text x="659" y="226" text-anchor="middle" class="cta-text" font-size="23">Free Estimates</text>
    <circle cx="144" cy="195" r="5" fill="var(--orange)"/>
    <text x="155" y="201" class="brand-name" font-size="16">Ridgeline Rails</text>
    <use href="#phone-icon" x="157" y="210" width="15" height="15"/>
    <text x="180" y="224" class="contact" font-size="16">555-316-2047</text>
    <use href="#mail-icon" x="157" y="234" width="16" height="12"/>
    <text x="180" y="247" class="contact" font-size="16">office@myridgelinerails.example</text>
  </g>

  <!-- Homepage ad -->
  <g class="homepage-ad">
    <rect x="73" y="291" width="900" height="150" fill="url(#mist)" role="img" aria-label="Faded photo of trees behind a white vinyl fence"/>
    <polygon points="655,291 973,291 973,441 610,441" fill="url(#wood)" role="img" aria-label="Photo of a scalloped wooden fence"/>
    <rect x="73" y="425" width="500" height="7" fill="var(--brown)"/>
    <rect x="73" y="432" width="520" height="9" fill="var(--orange)"/>
    <polygon points="555,350 585,350 545,441 515,441" fill="var(--brown)"/>
    <polygon points="605,291 620,291 555,441 540,441" fill="var(--blue)"/>
    <polygon points="618,291 720,291 665,441 553,441" fill="var(--orange)" opacity="0.9"/>
    <rect x="684" y="343" width="251" height="52" class="cta-frame"/>
    <text x="809" y="380" text-anchor="middle" class="cta-text" font-size="29">Free Estimates</text>
    <circle cx="166" cy="341" r="6" fill="var(--orange)"/>
    <text x="179" y="348" class="brand-name" font-size="20">Ridgeline Rails</text>
    <use href="#phone-icon" x="181" y="359" width="18" height="18"/>
    <text x="209" y="376" class="contact" font-size="20">555-316-2047</text>
    <use href="#mail-icon" x="180" y="390" width="20" height="15"/>
    <text x="209" y="405" class="contact" font-size="20">office@myridgelinerails.example</text>
  </g>

  <!-- Search results icon -->
  <g class="search-icon">
    <circle cx="70" cy="518" r="24" fill="none" stroke="var(--blue)" stroke-width="9"/>
    <path d="M60 508a14 14 0 0 1 14-6" fill="none" stroke="var(--blue)" stroke-width="4" stroke-linecap="round"/>
    <line x1="88" y1="536" x2="110" y2="556" stroke="var(--blue)" stroke-width="12" stroke-linecap="round"/>
  </g>

  <!-- Logo with phone -->
  <g class="logo-lockup">
    <circle cx="112" cy="648" r="8" fill="var(--orange)"/>
    <text x="130" y="657" class="brand-name" font-size="28">Ridgeline Rails</text>
    <text x="130" y="689" class="phone-bold" font-size="26" textLength="198" lengthAdjust="spacingAndGlyphs">555-316-2047</text>
    <text x="130" y="708" class="tagline" font-size="8.5" textLength="235" lengthAdjust="spacingAndGlyphs">"Because Good Fences Make Good Neighbors"</text>
  </g>

  <!-- Logo stand-in -->
  <g class="logo-badge">
    <circle cx="56" cy="757" r="10" fill="var(--orange)"/>
    <text x="44" y="800" class="brand-name-dark" font-size="22">Ridgeline</text>
    <text x="44" y="826" class="brand-name-dark" font-size="22">Rails</text>
  </g>

  <!-- Small logo -->
  <g class="logo-small">
    <circle cx="78" cy="866" r="6" fill="var(--orange)"/>
    <text x="90" y="873" class="brand-name" font-size="21">Ridgeline</text>
    <text x="90" y="900" class="brand-name" font-size="21">Rails</text>
  </g>

  <!-- Thumbnails -->
  <g class="thumbnails">
    <rect x="431" y="466" width="150" height="150" fill="var(--orange)"/>
    <rect x="439" y="474" width="134" height="134" fill="url(#vinyl)" role="img" aria-label="Photo of a white vinyl fence with a shrub"/>
    <rect x="431" y="637" width="150" height="150" fill="var(--brown)"/>
    <rect x="439" y="645" width="134" height="134" fill="url(#vinyl)" role="img" aria-label="Photo of a white vinyl fence with a shrub"/>
    <rect x="431" y="809" width="150" height="150" fill="var(--blue)"/>
    <rect x="439" y="817" width="134" height="134" fill="url(#vinyl)" role="img" aria-label="Photo of a white vinyl fence with a shrub"/>
  </g>

  <!-- Member page photo -->
  <g class="member-card">
    <rect x="629" y="463" width="503" height="502" fill="url(#wood)" role="img" aria-label="Photo of a scalloped wooden fence"/>
    <polygon points="868,463 1132,463 1132,965 870,965 740,688" fill="var(--orange)"/>
    <polygon points="918,463 1132,463 1132,923 918,923 818,688" fill="var(--white)"/>
    <polygon points="646,965 763,705 875,965" fill="var(--blue)"/>
    <rect x="919" y="516" width="169" height="236" fill="url(#portrait)" role="img" aria-label="Portrait photo of the chamber member"/>
    <text x="1008" y="810" text-anchor="middle" class="member-name" font-size="44">Sam Reed</text>
    <text x="1008" y="857" text-anchor="middle" class="member-role" font-size="38">Member</text>
  </g>
</svg>
</body>
</html>
```